Business Cards Needed for Innovative Healthcare Marketing Company

We are a marketing company focused on healthcare. Our company is all about rebranding yourself renewing your image and generating results. The phoenix stands for "reborn" or "rising" which we provide new brands for our clients we take their old brands and renew it with creativity and innovation. I am looking for a business card with color dimension. I have attached an example of a card I think has the look and feel of what I am trying to accomplish. I like that the card example has black and grey font colors, I like the font placement and the small logo, I really like the use of the colors on the right those are the colors of my logo. My logo is phoenix so maybe incorporating flames similar to that design. I would like the back a solid color maybe red with an opaque version of the logo and website. As a marketing company I am always open to creative liberty!

Target Market(s)

Doctors and business professionals.

Industry/Entity Type

Marketing

Contact Information for Business Card

Vornaly Health Care Marketing
Marnie Okonski- CEO
#(502)638-2947
email-marnie@vornaly.com
website- vornaly.com

Font styles to use
Sans Serif

Colors
ec1f27
f37122
ffc214
fbed22
fbf289
f04a50

Requirements
Must have
• The logo and required information
Nice to have
• icons by the information
Should not have
• child like font

```html
<!DOCTYPE html>
<html lang="en">
<head>
<meta charset="utf-8">
<title>Vornaly Health Care Marketing – Business Card</title>
<link href="https://fonts.googleapis.com/css2?family=Raleway:wght@300;400&family=Open+Sans:wght@400;700&display=swap" rel="stylesheet">
<style>
  :root {
    --red: #ec1f27;
    --red-soft: #f04a50;
    --orange: #f37122;
    --gold: #ffc214;
    --cream: #f1ede2;
    --charcoal: #2a2826;
    --ink: #2b2b2b;
    --grey: #555;
    --stage: #d6d5d2;
  }
  * { margin: 0; padding: 0; box-sizing: border-box; }
  html, body { width: 1200px; height: 786px; overflow: hidden; }
  body {
    background: var(--stage);
    display: flex;
    align-items: center;
    justify-content: center;
    gap: 40px;
    font-family: "Open Sans", sans-serif;
  }
  .card {
    position: relative;
    width: 540px;
    height: 309px;
    border-radius: 16px;
    overflow: hidden;
    box-shadow: 0 10px 30px rgba(0,0,0,.25);
  }
  /* Front */
  .card--front { background: var(--cream); }
  .brand {
    position: absolute;
    display: flex;
    align-items: center;
    gap: 12px;
  }
  .brand__mark {
    width: 34px; height: 34px;
    border-radius: 50%;
    background: var(--orange);
    flex: none;
  }
  .brand__name {
    font-family: "Raleway", sans-serif;
    font-weight: 300;
    color: var(--red);
    letter-spacing: 2px;
    line-height: 1;
  }
  .brand__tag {
    font-family: "Raleway", sans-serif;
    font-weight: 400;
    color: var(--red-soft);
    letter-spacing: 1.5px;
    text-transform: uppercase;
    padding-top: 4px;
    border-top: 1px solid var(--red-soft);
    margin-top: 5px;
  }
  .card--front .brand { left: 150px; top: 40px; }
  .card--front .brand__name { font-size: 38px; }
  .card--front .brand__tag { font-size: 9px; }

  .person { position: absolute; left: 40px; top: 126px; }
  .person__name {
    font-weight: 700; font-size: 17px; color: var(--ink);
    text-transform: uppercase; letter-spacing: .5px;
  }
  .person__role { font-size: 13px; color: var(--grey); margin-top: 2px; }

  .contact { position: absolute; left: 40px; top: 190px; list-style: none; }
  .contact li {
    display: flex; align-items: center; gap: 9px;
    font-size: 13px; color: var(--ink); margin-bottom: 7px;
  }
  .contact__icon {
    width: 16px; height: 16px; border-radius: 3px;
    background: var(--orange);
    display: flex; align-items: center; justify-content: center;
  }
  .front-art {
    position: absolute; right: 0; bottom: 0;
    width: 250px; height: 240px;
    border-top-left-radius: 140px 160px;
    background: linear-gradient(200deg, var(--red) 0%, var(--orange) 70%, var(--gold) 100%);
    opacity: .9;
  }

  /* Back */
  .card--back { background: var(--charcoal); }
  .back-art {
    position: absolute; left: 0; top: 0;
    width: 300px; height: 150px;
    border-bottom-right-radius: 260px 150px;
    background: linear-gradient(120deg, var(--orange) 0%, var(--red) 60%, var(--red-soft) 100%);
    opacity: .9;
  }
  .card--back .brand {
    left: 210px; top: 150px;
    flex-direction: column; align-items: flex-start; gap: 8px;
  }
  .card--back .brand__mark { width: 30px; height: 30px; margin-left: 70px; }
  .card--back .brand__name { font-size: 40px; }
  .card--back .brand__tag { font-size: 9px; }
  .back-web {
    position: absolute; left: 230px; top: 262px;
    font-size: 13px; color: var(--orange); letter-spacing: .5px;
  }
</style>
</head>
<body>
  <section class="card card--front">
    <div class="brand">
      <span class="brand__mark"></span>
      <div>
        <div class="brand__name">VORNALY</div>
        <div class="brand__tag">Health Care Marketing</div>
      </div>
    </div>

    <div class="person">
      <div class="person__name">Marnie Okonski</div>
      <div class="person__role">CEO</div>
    </div>

    <ul class="contact">
      <li><span class="contact__icon">
        <svg width="10" height="10" viewBox="0 0 24 24"><path fill="#fff" d="M6.6 10.8a15 15 0 0 0 6.6 6.6l2.2-2.2c.3-.3.7-.4 1-.2 1.1.4 2.3.6 3.6.6.6 0 1 .4 1 1V20c0 .6-.4 1-1 1A17 17 0 0 1 3 4c0-.6.4-1 1-1h3.5c.6 0 1 .4 1 1 0 1.3.2 2.5.6 3.6.1.3 0 .7-.2 1z"/></svg>
      </span>(502)638-2947</li>
      <li><span class="contact__icon">
        <svg width="10" height="10" viewBox="0 0 24 24"><path fill="#fff" d="M2 5h20v14H2z"/><path fill="none" stroke="#f37122" stroke-width="2" d="M2 5l10 8 10-8"/></svg>
      </span>marnie@vornaly.com</li>
      <li><span class="contact__icon">
        <svg width="10" height="10" viewBox="0 0 24 24"><circle cx="12" cy="12" r="9" fill="none" stroke="#fff" stroke-width="2.5"/><path stroke="#fff" stroke-width="2" d="M3 12h18M12 3v18"/></svg>
      </span>www.vornaly.com</li>
    </ul>

    <div class="front-art" role="img" aria-label="Large phoenix illustration in red and orange"></div>
  </section>

  <section class="card card--back">
    <div class="back-art" role="img" aria-label="Flame-coloured phoenix wing illustration"></div>
    <div class="brand">
      <span class="brand__mark"></span>
      <div>
        <div class="brand__name">VORNALY</div>
        <div class="brand__tag">Health Care Marketing</div>
      </div>
    </div>
    <div class="back-web">www.vornaly.com</div>
  </section>
</body>
</html>
```